update Coffeeshop menu design to be more modern and luxury

I want a menu that compliments the colors of the shop. I want a simple nice clean modern looking menu. The text is available on old menu (drinks) and the word document attached (food)

We changed the interior of our shop and want the new menu to reflect the new look and feel (see pictures attached). This project is a template menu therefore it should give us the ability to add content. Keep in mind that we want the layout to be one page . one side in english and the other in Arabic (we will update the arabic side to match the english design)
Updates

Project Deadline Extended
Reason: Now more information is provided including text and samples on old menu. The brand name is Brewvant.

Industry/Entity Type

Coffee Shop

Font styles to use
Sans Serif

Colors

Designer to choose colors to be used in the design.

Requirements
Must have
• My menu must have clean modern look that matches the shop style. It should have the logo of the coffee shop (provided). we would like a one pager menu one ideally (double sided) with variant in a3 and a4
• The design will be a template that we can update with content (content is not final). I attached the current menu for reference although content will be changed.
Nice to have
• Simple, attractive, easy to read, luxury modern.
Should not have
• Should not be crowded. no folds. no need for images. should not look like the old menu

```html
<!DOCTYPE html>
<html lang="en">
<head>
<meta charset="utf-8">
<title>Brewvant Menu</title>
<link href="https://fonts.googleapis.com/css2?family=Montserrat:wght@400;500;600;700;800&display=swap" rel="stylesheet">
<style>
  :root {
    --ink: #333132;
    --ink-soft: #55514f;
    --gold: #d6a94a;
    --pattern: #d8d2cc;
    --paper: #ffffff;
    --muted: #9a948f;
  }
  * { box-sizing: border-box; margin: 0; padding: 0; }
  html, body { width: 849px; height: 1200px; overflow: hidden; background: var(--paper); }
  body { font-family: 'Montserrat', sans-serif; color: var(--ink); position: relative; }

  .border-pattern {
    position: absolute; inset: 0;
    background: linear-gradient(135deg, #e2ddd8, var(--pattern));
  }
  .sheet {
    position: absolute; left: 71px; top: 68px; width: 707px; height: 1062px;
    background: var(--paper);
  }
  .brand-badge {
    position: absolute; left: 376px; top: 10px; width: 98px; height: 98px;
    border-radius: 50%; background: var(--paper);
    border: 3px solid var(--gold);
    display: flex; align-items: center; justify-content: center;
    font-weight: 700; font-size: 16px; color: var(--ink); z-index: 2;
  }

  .menu-section { position: absolute; width: 230px; }
  .col-left { left: 133px; }
  .col-right { left: 460px; }
  .section-title {
    font-size: 21px; font-weight: 800; letter-spacing: 1px; text-transform: uppercase;
    line-height: 1;
  }
  .section-rule { height: 2px; background: var(--gold); margin: 8px 0 4px; width: 230px; }
  .size-labels {
    display: flex; justify-content: flex-end; gap: 14px;
    font-size: 5.5px; font-weight: 600; color: var(--muted); letter-spacing: .4px;
    margin-bottom: 2px; padding-right: 2px;
  }
  .item {
    display: flex; align-items: center; height: 18.5px;
    font-size: 10.5px; font-weight: 600; text-transform: uppercase; letter-spacing: .3px;
  }
  .item .name { flex: 1; }
  .item .price { width: 28px; text-align: right; font-weight: 600; color: var(--ink-soft); }
  .item.gap { height: 10px; }

  .footer {
    position: absolute; left: 120px; top: 1095px; width: 610px;
    display: flex; justify-content: space-between; align-items: center;
    font-size: 8px; font-weight: 500; letter-spacing: .6px; color: var(--ink-soft);
    text-transform: uppercase;
  }
  .footer-link { display: flex; align-items: center; gap: 7px; }
  .footer-link .dot { width: 15px; height: 15px; border-radius: 50%; background: var(--ink); }
</style>
</head>
<body>
  <div class="border-pattern" role="img" aria-label="Light grey chevron zigzag pattern framing the menu"></div>
  <div class="sheet"></div>
  <div class="brand-badge">Brewvant</div>

  <section class="menu-section col-left" style="top:110px">
    <h2 class="section-title">Hot Beverages</h2>
    <div class="section-rule"></div>
    <div class="size-labels"><span>SMALL</span><span>LARGE</span></div>
    <div class="item"><span class="name">Espresso</span><span class="price">11</span><span class="price">13</span></div>
    <div class="item"><span class="name">Espresso con panna</span><span class="price">14</span><span class="price">16</span></div>
    <div class="item"><span class="name">Espresso macchiato</span><span class="price">13</span><span class="price">15</span></div>
    <div class="item"><span class="name">Turkish coffee</span><span class="price">11</span><span class="price">13</span></div>
  </section>

  <section class="menu-section col-left" style="top:272px">
    <h2 class="section-title">Hot Coffee</h2>
    <div class="section-rule"></div>
    <div class="size-labels"><span>REGULAR</span><span>LARGE</span></div>
    <div class="item"><span class="name">Americano</span><span class="price">15</span><span class="price">17</span></div>
    <div class="item"><span class="name">Cappuccino</span><span class="price">17</span><span class="price">19</span></div>
    <div class="item"><span class="name">Cafe latte</span><span class="price">17</span><span class="price">19</span></div>
    <div class="item"><span class="name">Dark mocha</span><span class="price">19</span><span class="price">21</span></div>
    <div class="item"><span class="name">Caramel macchiato</span><span class="price">21</span><span class="price">24</span></div>
    <div class="item"><span class="name">Hot chocolate</span><span class="price">19</span><span class="price">21</span></div>
    <div class="item"><span class="name">Flat white</span><span class="price">17</span><span class="price"></span></div>
    <div class="item"><span class="name">Arabic coffee</span><span class="price">19</span><span class="price"></span></div>
    <div class="item"><span class="name">Hot milk</span><span class="price">13</span><span class="price">15</span></div>
    <div class="item"><span class="name">Tiramisu latte</span><span class="price">19</span><span class="price">21</span></div>
    <div class="item"><span class="name">Double mocha</span><span class="price">19</span><span class="price">21</span></div>
  </section>

  <section class="menu-section col-left" style="top:560px">
    <h2 class="section-title">Gourmet Tea</h2>
    <div class="section-rule"></div>
    <div class="size-labels"><span>REGULAR</span><span>LARGE</span></div>
    <div class="item"><span class="name">English breakfast tea</span><span class="price">15</span><span class="price">17</span></div>
    <div class="item"><span class="name">Earl grey tea</span><span class="price">15</span><span class="price">17</span></div>
    <div class="item"><span class="name">Peppermint tea</span><span class="price">15</span><span class="price">17</span></div>
    <div class="item"><span class="name">Camomile tea</span><span class="price">15</span><span class="price">17</span></div>
    <div class="item"><span class="name">Green tea</span><span class="price">15</span><span class="price">17</span></div>
    <div class="item"><span class="name">Chai tea latte</span><span class="price">19</span><span class="price">21</span></div>
  </section>

  <section class="menu-section col-left" style="top:785px">
    <h2 class="section-title">Frappevant</h2>
    <div class="section-rule"></div>
    <div class="size-labels"><span>REGULAR</span><span>LARGE</span></div>
    <div class="item"><span class="name">Brewvant frappe</span><span class="price">22</span><span class="price">24</span></div>
    <div class="item"><span class="name">Dark mocha frappe</span><span class="price">20</span><span class="price">22</span></div>
    <div class="item"><span class="name">Chocolate frappe</span><span class="price">20</span><span class="price">22</span></div>
    <div class="item"><span class="name">Vanilla frappe</span><span class="price">20</span><span class="price">22</span></div>
    <div class="item"><span class="name">Mango frappe</span><span class="price">20</span><span class="price">22</span></div>
    <div class="item"><span class="name">Strawberry frappe</span><span class="price">21</span><span class="price">23</span></div>
    <div class="item"><span class="name">Double mocha frappe</span><span class="price">20</span><span class="price">22</span></div>
    <div class="item"><span class="name">Cookie cream frappe</span><span class="price">20</span><span class="price">22</span></div>
    <div class="item"><span class="name">Coffee crumble frappe</span><span class="price">20</span><span class="price">22</span></div>
  </section>

  <section class="menu-section col-right" style="top:110px">
    <h2 class="section-title">Coffee on Ice</h2>
    <div class="section-rule"></div>
    <div class="size-labels"><span>REGULAR</span><span>LARGE</span></div>
    <div class="item"><span class="name">Iced americano</span><span class="price">17</span><span class="price">19</span></div>
    <div class="item"><span class="name">Iced cappuccino</span><span class="price">19</span><span class="price">21</span></div>
    <div class="item"><span class="name">Iced latte</span><span class="price">19</span><span class="price">21</span></div>
    <div class="item"><span class="name">Iced caramel macchiato</span><span class="price">21</span><span class="price">23</span></div>
    <div class="item"><span class="name">Caramel macchiato</span><span class="price">19</span><span class="price">21</span></div>
    <div class="item"><span class="name">Iced mocha</span><span class="price">19</span><span class="price">21</span></div>
    <div class="item"><span class="name">Iced chocolate</span><span class="price">19</span><span class="price">21</span></div>
    <div class="item"><span class="name">Iced milk</span><span class="price">13</span><span class="price">15</span></div>
    <div class="item"><span class="name">Iced shaken espresso</span><span class="price">17</span><span class="price">19</span></div>
  </section>

  <section class="menu-section col-right" style="top:372px">
    <h2 class="section-title">Iced Gourmet Tea</h2>
    <div class="section-rule"></div>
    <div class="size-labels"><span>REGULAR</span><span>LARGE</span></div>
    <div class="item"><span class="name">Iced green tea</span><span class="price">15</span><span class="price">17</span></div>
    <div class="item"><span class="name">Iced green tea mint</span><span class="price">15</span><span class="price">17</span></div>
    <div class="item"><span class="name">Iced camomile</span><span class="price">15</span><span class="price">17</span></div>
    <div class="item"><span class="name">Iced cucumber lemon</span><span class="price">17</span><span class="price">19</span></div>
    <div class="item"><span class="name">Iced peach tea</span><span class="price">17</span><span class="price">19</span></div>
    <div class="item"><span class="name">Iced lemon tea</span><span class="price">17</span><span class="price">19</span></div>
  </section>

  <section class="menu-section col-right" style="top:573px">
    <h2 class="section-title">Juices &amp; Frosties</h2>
    <div class="section-rule"></div>
    <div class="size-labels"><span>REGULAR</span><span>LARGE</span></div>
    <div class="item"><span class="name">Citrus frostie</span><span class="price">17</span><span class="price">19</span></div>
    <div class="item"><span class="name">Strawberry frostie</span><span class="price">21</span><span class="price">23</span></div>
    <div class="item"><span class="name">Lychee frostie</span><span class="price">19</span><span class="price">21</span></div>
    <div class="item"><span class="name">Orange juice</span><span class="price">17</span><span class="price">21</span></div>
    <div class="item"><span class="name">Lemon and mint juice</span><span class="price">13</span><span class="price">15</span></div>
  </section>

  <section class="menu-section col-right" style="top:785px">
    <h2 class="section-title">Variety &amp; Extras</h2>
    <div class="section-rule"></div>
    <div class="size-labels"><span>REGULAR</span><span>LARGE</span></div>
    <div class="item"><span class="name">Italian soda</span><span class="price">19</span><span class="price">21</span></div>
    <div class="item gap"></div>
    <div class="item"><span class="name">Spring water</span><span class="price"></span><span class="price">18</span></div>
    <div class="item"><span class="name">Brewvant water</span><span class="price"></span><span class="price">5</span></div>
    <div class="item"><span class="name">Sparkling water</span><span class="price"></span><span class="price">15</span></div>
    <div class="item"><span class="name">Extra shot</span><span class="price"></span><span class="price">4</span></div>
    <div class="item"><span class="name">Syrup</span><span class="price"></span><span class="price">4</span></div>
    <div class="item gap"></div>
    <div class="item"><span class="name">Whipped cream</span><span class="price"></span><span class="price">4</span></div>
    <div class="item"><span class="name">Chocolate sauce</span><span class="price"></span><span class="price">4</span></div>
    <div class="item"><span class="name">Caramel sauce</span><span class="price"></span><span class="price">4</span></div>
    <div class="item"><span class="name">Almond milk</span><span class="price"></span><span class="price">4</span></div>
    <div class="item"><span class="name">Soya milk</span><span class="price"></span><span class="price">4</span></div>
  </section>

  <footer class="footer">
    <div class="footer-link"><span class="dot"></span><span>@brewvantcitycafe</span></div>
    <div class="footer-link"><span class="dot"></span><span>@brewvanthouse</span></div>
    <div class="footer-link"><span class="dot"></span><span>www.brewvant-cafe.com</span></div>
  </footer>
</body>
</html>
```